Coral Ridge Networks Ltd

I need a website that is an informational only. We are a construction business building telecommunications sites. Seeing how our company is Coral Ridge the color blue might want to be incorporated in the color scheme.
I can provide more picture of towers and wireless communications if needed.
current website www.coralridgenet.ca

Industry/Entity Type

Wireless Telecommunications, Construction

Coding

Coded - Design and coding required

Number of Pages Required

2 page

Font styles to use
Sans Serif

Colors

Designer to choose colors to be used in the design.

```html
<!DOCTYPE html>
<html lang="en">
<head>
<meta charset="utf-8">
<title>Coral Ridge Networks Ltd</title>
<link rel="stylesheet" href="https://fonts.googleapis.com/css2?family=Montserrat:wght@400;500;600;700&family=Open+Sans:wght@400;600&display=swap">
<style>
:root{
  --blue:#1f6fc5;
  --blue-dark:#15589f;
  --navy:#0e1e30;
  --ink:#1d2733;
  --text:#5b6673;
  --light:#f3f5f8;
  --line:#dfe4ea;
  --footer:#1f2124;
  --white:#ffffff;
  --star:#1f6fc5;
}
*{margin:0;padding:0;box-sizing:border-box}
html,body{width:1200px;height:3764px;overflow:hidden}
body{font-family:"Open Sans",Arial,sans-serif;color:var(--text);background:var(--white);position:relative}
.abs{position:absolute}
h1,h2,h3,.head{font-family:"Montserrat",Arial,sans-serif}

/* hero */
.hero{position:absolute;left:0;top:0;width:1200px;height:520px;
  background:linear-gradient(180deg,#3b4d63 0%,#55677c 45%,#2c3a4c 100%)}
.hero::after{content:"";position:absolute;inset:0;background:rgba(14,30,48,.55)}
.hero *{position:relative;z-index:1}
.brand-box{position:absolute;left:140px;top:16px;width:108px;height:64px;background:var(--white);display:flex;align-items:center;justify-content:center;z-index:2}
.brand-box span{font-family:"Montserrat",sans-serif;font-weight:700;font-size:17px;color:var(--blue)}
.nav{position:absolute;right:136px;top:36px;display:flex;gap:34px;align-items:center;z-index:2}
.nav a{color:var(--white);font-family:"Montserrat",sans-serif;font-size:14px;text-decoration:none}
.nav a.active{font-weight:700}
.nav .btn{border:1.5px solid var(--white);padding:8px 20px}
.hero-kicker{position:absolute;left:0;width:1200px;top:234px;text-align:center;z-index:2}
.hero-kicker span{background:var(--blue);color:var(--white);font-family:"Montserrat",sans-serif;font-weight:600;font-size:16px;letter-spacing:2px;padding:4px 14px}
.hero-title{position:absolute;left:0;width:1200px;top:272px;text-align:center;color:var(--white);font-weight:700;font-size:40px;line-height:48px;letter-spacing:1px;z-index:2}
.dots{position:absolute;display:flex;flex-direction:column;gap:14px;z-index:2}
.dots i{width:10px;height:10px;border-radius:50%;background:rgba(255,255,255,.55);display:block}
.dots i.on{background:var(--white)}
.scroll-cue{position:absolute;left:580px;top:500px;width:40px;height:40px;border-radius:50%;background:var(--white);border:2px solid var(--blue);z-index:3;display:flex;align-items:center;justify-content:center}

/* about */
.about{position:absolute;left:0;top:520px;width:1200px;height:620px;background:var(--light)}
.kicker{font-family:"Montserrat",sans-serif;font-size:12px;font-weight:600;letter-spacing:1.5px;color:var(--blue);text-transform:uppercase}
.title{font-family:"Montserrat",sans-serif;font-weight:600;font-size:34px;color:var(--ink)}
.body-p{font-size:13.5px;line-height:22px;color:var(--text)}
.about .copy{position:absolute;left:228px;top:124px;width:420px}
.about .copy .title{margin:6px 0 28px}
.about .copy .body-p{margin-bottom:16px}
.about .lead{font-size:16px;line-height:24px;color:var(--ink);margin-top:14px}
.about .call{margin-top:30px;font-size:12px;color:var(--blue)}
.about .phone{display:flex;align-items:center;gap:8px;margin-top:6px;font-family:"Montserrat",sans-serif;font-weight:600;font-size:20px;color:var(--ink)}
.photo{position:absolute}
.badge{position:absolute;left:740px;top:152px;width:84px;height:86px;background:var(--ink);color:var(--white);text-align:center;padding-top:10px;z-index:2}
.badge b{font-family:"Montserrat",sans-serif;font-size:34px;display:block;line-height:38px}
.badge small{font-family:"Montserrat",sans-serif;font-size:12px;letter-spacing:2px}

/* why */
.why{position:absolute;left:0;top:1140px;width:1200px;height:640px;background:var(--white)}
.why .copy{position:absolute;left:452px;top:136px;width:560px}
.why .copy .title{margin:4px 0 18px}
.features{position:absolute;left:452px;top:350px;width:600px;display:grid;grid-template-columns:368px 232px;row-gap:22px}
.feature{display:flex;gap:14px;align-items:flex-start;font-size:13px;line-height:19px;color:var(--ink)}
.feature svg{flex:0 0 30px}

/* services */
.services{position:absolute;left:0;top:1780px;width:1200px;height:620px;background:var(--white)}
.center-head{position:absolute;left:0;width:1200px;text-align:center}
.panel{position:absolute;top:212px;height:408px;width:400px}
.panel-label{position:absolute;bottom:28px;display:flex;flex-direction:column;align-items:center;gap:10px;color:var(--white);font-family:"Montserrat",sans-serif;font-weight:600;font-size:18px;letter-spacing:1px}
.ring{width:44px;height:44px;border-radius:50%;border:2px solid var(--white);display:flex;align-items:center;justify-content:center}
.panel-feature{position:absolute;left:400px;top:192px;width:400px;height:428px;background:linear-gradient(180deg,rgba(31,111,197,.92),rgba(21,88,159,.95)),#1f6fc5;box-shadow:0 10px 30px rgba(0,0,0,.25);text-align:center;color:var(--white);z-index:2}
.panel-feature h3{font-size:22px;font-weight:600;letter-spacing:1px;line-height:28px;margin-top:186px}
.panel-feature p{font-size:13px;line-height:20px;width:290px;margin:14px auto 0;color:rgba(255,255,255,.85)}

/* reviews */
.reviews{position:absolute;left:0;top:2400px;width:1200px;height:560px;background:var(--white)}
.review{position:absolute;top:220px;width:420px;height:160px;display:flex;gap:22px}
.review .face{width:140px;height:160px;flex:0 0 140px}
.review .quote{font-family:"Montserrat",sans-serif;font-size:40px;line-height:30px;color:var(--ink);font-weight:700}
.review p{font-size:12px;line-height:18px;color:var(--text);margin-top:6px}
.review .name{font-family:"Montserrat",sans-serif;font-weight:600;font-size:13px;color:var(--ink);margin-top:12px}
.stars{display:flex;gap:3px;margin-top:4px}
.arrows{position:absolute;left:540px;top:440px;display:flex;gap:24px}
.arrows span{width:44px;height:44px;border-radius:50%;display:flex;align-items:center;justify-content:center}
.arrows .prev{background:var(--light)}
.arrows .next{background:var(--white);box-shadow:0 2px 10px rgba(0,0,0,.15)}

/* contact */
.contact{position:absolute;left:0;top:2960px;width:1200px;height:480px;background:linear-gradient(180deg,#1b2735 0%,#2a3645 55%,#151c25 100%)}
.contact::after{content:"";position:absolute;inset:0;background:rgba(10,16,24,.45)}
.contact > *{z-index:1}
.contact .lead-block{position:absolute;left:160px;top:116px;width:340px;color:var(--white)}
.contact .kicker{color:var(--white)}
.contact h2{font-size:34px;font-weight:600;line-height:42px;margin-top:6px}
.contact .info{margin-top:44px;display:flex;flex-direction:column;gap:14px;font-size:12.5px;color:rgba(255,255,255,.85)}
.contact .info div{display:flex;gap:10px;align-items:flex-start}
.form{position:absolute;left:552px;top:122px;width:496px}
.field{background:var(--white);height:40px;font-size:12px;color:#8a939d;padding:11px 14px;position:absolute}
.send{position:absolute;left:0;top:246px;background:var(--blue);color:var(--white);font-family:"Montserrat",sans-serif;font-size:12px;font-weight:600;padding:10px 18px}

/* footer */
.footer{position:absolute;left:0;top:3440px;width:1200px;height:324px;background:var(--footer);color:rgba(255,255,255,.75);font-size:12px}
.footer .brand-box{left:160px;top:40px;width:152px;height:112px}
.footer .brand-box span{font-size:22px}
.fcol{position:absolute;top:56px}
.fcol h4{font-family:"Montserrat",sans-serif;font-weight:600;font-size:15px;color:var(--white);margin-bottom:14px}
.fcol li{list-style:none;line-height:22px}
.fcol .row{display:flex;gap:8px;align-items:center;line-height:24px}
.socials{display:flex;gap:6px;margin-top:12px}
.socials i{width:22px;height:22px;background:var(--blue);display:block}
.copyright{position:absolute;left:0;width:1200px;top:282px;text-align:center;font-size:11px;color:rgba(255,255,255,.55)}
.rule{position:absolute;left:160px;width:880px;top:258px;height:1px;background:rgba(255,255,255,.12)}
</style>
</head>
<body>

<header class="hero" role="img" aria-label="Photo of telecommunications towers and rooftop antennas against a mountain skyline">
  <div class="brand-box"><span>Coral Ridge</span></div>
  <nav class="nav">
    <a class="active">Home</a>
    <a>About Us</a>
    <a>Services</a>
    <a class="btn">Contact</a>
  </nav>
  <div class="dots" style="left:40px;top:276px"><i class="on"></i><i></i><i></i></div>
  <div class="dots" style="left:1112px;top:112px"><i class="on"></i><i></i></div>
  <div class="hero-kicker"><span>WE ARE A</span></div>
  <h1 class="hero-title">CONSTRUCTION BUSINESS BUILDING<br>TELECOMMUNICATIONS SITES</h1>
</header>
<div class="scroll-cue">
  <svg width="14" height="20" viewBox="0 0 14 20"><rect x="1" y="1" width="12" height="18" rx="6" fill="none" stroke="#1f6fc5" stroke-width="2"/><line x1="7" y1="5" x2="7" y2="9" stroke="#1f6fc5" stroke-width="2"/></svg>
</div>

<section class="about">
  <div class="copy">
    <div class="kicker">Welcome to</div>
    <h2 class="title">Coral Ridge</h2>
    <p class="body-p">At <span style="color:var(--blue)">Coral Ridge Ltd.</span> we are dedicated to providing our customers with friendly professional service. We value your business. We have made it our mission to provide reliable products and services in our customer-driven approach.</p>
    <p class="body-p">Our courteous, professional team is able to support a range of services to meet your requirements.</p>
    <p class="lead">To learn more about Coral Ridge Ltd. and the products and services we can offer</p>
    <div class="call">Please call us at</div>
    <div class="phone">
      <svg width="18" height="18" viewBox="0 0 24 24"><path d="M6.6 10.8a15 15 0 0 0 6.6 6.6l2.2-2.2a1 1 0 0 1 1-.25 11.4 11.4 0 0 0 3.6.57 1 1 0 0 1 1 1V20a1 1 0 0 1-1 1A17 17 0 0 1 3 4a1 1 0 0 1 1-1h3.5a1 1 0 0 1 1 1c0 1.25.2 2.45.57 3.57a1 1 0 0 1-.25 1z" fill="#1f6fc5"/></svg>
      1-604-555-0148
    </div>
  </div>
  <div class="photo" role="img" aria-label="Photo of a lattice telecommunications tower against a blue sky" style="left:712px;top:120px;width:280px;height:360px;background:linear-gradient(180deg,#9fc3e6,#4f80b4 60%,#3b5f86)"></div>
  <div class="badge"><b>15</b><small>YEARS</small></div>
  <div class="photo" role="img" aria-label="Photo of technicians working on antennas at the top of a tower" style="left:620px;top:428px;width:212px;height:132px;background:linear-gradient(160deg,#c9d6e2,#7c8fa3);border:6px solid var(--white)"></div>
</section>

<section class="why">
  <div class="photo" role="img" aria-label="Photo of a tall steel telecommunications tower with antennas" style="left:0;top:0;width:388px;height:640px;background:linear-gradient(180deg,#dfe7ee,#9aa9b8 55%,#56687b)"></div>
  <div class="copy">
    <div class="kicker">Why choose</div>
    <h2 class="title">Coral Ridge</h2>
    <p class="body-p" style="font-size:12.5px;line-height:20px">At Coral Ridge Networks Ltd safety is number one. Coral Ridge Ltd is committed to a strong safety policy, protecting its staff and the general public from accidents and harm. All Coral Ridge employees are certified "Tower Competent Climber and Rescue" in addition to water safety and fall protection. Coral Ridge's safety training and practices include but are not limited to the following:</p>
  </div>
  <div class="features">
    <div class="feature"><svg width="30" height="30" viewBox="0 0 30 30"><rect x="1" y="1" width="28" height="28" fill="none" stroke="#1f6fc5" stroke-width="2"/><path d="M9 15l4 4 8-8" fill="none" stroke="#1f6fc5" stroke-width="2"/></svg><span>COR Certified</span></div>
    <div class="feature"><svg width="30" height="30" viewBox="0 0 30 30"><rect x="1" y="1" width="28" height="28" fill="none" stroke="#1f6fc5" stroke-width="2"/><path d="M9 15l4 4 8-8" fill="none" stroke="#1f6fc5" stroke-width="2"/></svg><span>BC Level 1 first aid</span></div>
    <div class="feature"><svg width="30" height="30" viewBox="0 0 30 30"><rect x="1" y="1" width="28" height="28" fill="none" stroke="#1f6fc5" stroke-width="2"/><path d="M9 15l4 4 8-8" fill="none" stroke="#1f6fc5" stroke-width="2"/></svg><span>Transportation Endorsement<br>first aid</span></div>
    <div class="feature"><svg width="30" height="30" viewBox="0 0 30 30"><rect x="1" y="1" width="28" height="28" fill="none" stroke="#1f6fc5" stroke-width="2"/><path d="M9 15l4 4 8-8" fill="none" stroke="#1f6fc5" stroke-width="2"/></svg><span>Sprat Level 1</span></div>
    <div class="feature"><svg width="30" height="30" viewBox="0 0 30 30"><rect x="1" y="1" width="28" height="28" fill="none" stroke="#1f6fc5" stroke-width="2"/><path d="M9 15l4 4 8-8" fill="none" stroke="#1f6fc5" stroke-width="2"/></svg><span>On-site tailboard meeting with<br>daily checklist sign off and<br>picture documentation</span></div>
    <div class="feature"><svg width="30" height="30" viewBox="0 0 30 30"><rect x="1" y="1" width="28" height="28" fill="none" stroke="#1f6fc5" stroke-width="2"/><path d="M9 15l4 4 8-8" fill="none" stroke="#1f6fc5" stroke-width="2"/></svg><span>Monthly in office safety<br>meetings</span></div>
    <div class="feature"><svg width="30" height="30" viewBox="0 0 30 30"><rect x="1" y="1" width="28" height="28" fill="none" stroke="#1f6fc5" stroke-width="2"/><path d="M9 15l4 4 8-8" fill="none" stroke="#1f6fc5" stroke-width="2"/></svg><span>Job site specific hazard<br>assessment and reporting</span></div>
  </div>
</section>

<section class="services">
  <div class="center-head" style="top:112px"><div class="kicker">Services</div><h2 class="title" style="margin-top:4px">Coral Ridge</h2></div>
  <div class="panel" role="img" aria-label="Photo of engineers in hard hats reviewing plans on a city rooftop" style="left:0;background:linear-gradient(180deg,#9eb0c2,#5f7388 60%,#2f3c4b)">
    <div class="panel-label" style="left:60px"><span class="ring"><svg width="14" height="14" viewBox="0 0 14 14"><path d="M3 7h8M8 4l3 3-3 3" fill="none" stroke="#fff" stroke-width="1.8"/></svg></span>ROOFTOP SITES</div>
  </div>
  <div class="panel-feature">
    <div class="ring" style="position:absolute;left:178px;top:100px"><svg width="18" height="20" viewBox="0 0 18 20"><path d="M9 2L4 18M9 2l5 16M6 11h6M9 2v16" fill="none" stroke="#fff" stroke-width="1.6"/></svg></div>
    <h3>TOWERS AND<br>MONOPOLES</h3>
    <p>Coral Ridge can engineer, supply and install all your tower needs, new structures or existing, we can provide the right solution for your site.</p>
    <div class="ring" style="position:absolute;left:178px;top:348px"><svg width="14" height="14" viewBox="0 0 14 14"><path d="M3 7h8M8 4l3 3-3 3" fill="none" stroke="#fff" stroke-width="1.8"/></svg></div>
  </div>
  <div class="panel" role="img" aria-label="Photo of in-building network equipment racks" style="left:800px;background:linear-gradient(180deg,#a8b3bd,#6b7884 55%,#38424d)">
    <div class="panel-label" style="left:112px"><span class="ring"><svg width="14" height="14" viewBox="0 0 14 14"><path d="M3 7h8M8 4l3 3-3 3" fill="none" stroke="#fff" stroke-width="1.8"/></svg></span>IN BUILDING</div>
  </div>
</section>

<section class="reviews">
  <div class="center-head" style="top:120px"><div class="kicker">Reviews</div><h2 class="title" style="margin-top:4px">Coral Ridge</h2></div>
  <div class="review" style="left:160px">
    <div class="face" role="img" aria-label="Portrait photo of a client" style="background:linear-gradient(180deg,#d6d9dc,#9ea4aa)"></div>
    <div>
      <div class="quote">“</div>
      <p>Their crew was safe, quick and careful on every site. Clear updates from start to finish and the work passed inspection first time.</p>
      <div class="name">Dana Morrow</div>
      <div class="stars"><svg width="80" height="12" viewBox="0 0 80 12"><g fill="#1f6fc5"><path id="s" d="M6 0l1.8 3.9 4.2.4-3.2 2.8 1 4.1L6 9 2.2 11.2l1-4.1L0 4.3l4.2-.4z"/><use href="#s" x="16"/><use href="#s" x="32"/><use href="#s" x="48"/><use href="#s" x="64"/></g></svg></div>
    </div>
  </div>
  <div class="review" style="left:620px">
    <div class="face" role="img" aria-label="Portrait photo of a client" style="background:linear-gradient(180deg,#d3d6da,#8f969d)"></div>
    <div>
      <div class="quote">“</div>
      <p>Their crew was safe, quick and careful on every site. Clear updates from start to finish and the work passed inspection first time.</p>
      <div class="name">Dana Morrow</div>
      <div class="stars"><svg width="80" height="12" viewBox="0 0 80 12"><g fill="#1f6fc5"><use href="#s"/><use href="#s" x="16"/><use href="#s" x="32"/><use href="#s" x="48"/><use href="#s" x="64"/></g></svg></div>
    </div>
  </div>
  <div class="arrows">
    <span class="prev"><svg width="14" height="14" viewBox="0 0 14 14"><path d="M11 7H3M6 4L3 7l3 3" fill="none" stroke="#1d2733" stroke-width="1.8"/></svg></span>
    <span class="next"><svg width="14" height="14" viewBox="0 0 14 14"><path d="M3 7h8M8 4l3 3-3 3" fill="none" stroke="#1d2733" stroke-width="1.8"/></svg></span>
  </div>
</section>

<section class="contact" role="img" aria-label="Dark photo of a telecommunications tower at dusk">
  <div class="lead-block">
    <div class="kicker">Contact us</div>
    <h2>How Can Coral Ridge Help You?</h2>
    <div class="info">
      <div><svg width="12" height="16" viewBox="0 0 12 16"><path d="M6 0a6 6 0 0 1 6 6c0 4-6 10-6 10S0 10 0 6a6 6 0 0 1 6-6z" fill="#1f6fc5"/><circle cx="6" cy="6" r="2" fill="#fff"/></svg><span>4120 Harbour Ave, Surrey, BC<br>V3S 2K7</span></div>
      <div><svg width="12" height="12" viewBox="0 0 24 24"><path d="M6.6 10.8a15 15 0 0 0 6.6 6.6l2.2-2.2a1 1 0 0 1 1-.25 11.4 11.4 0 0 0 3.6.57 1 1 0 0 1 1 1V20a1 1 0 0 1-1 1A17 17 0 0 1 3 4a1 1 0 0 1 1-1h3.5a1 1 0 0 1 1 1c0 1.25.2 2.45.57 3.57a1 1 0 0 1-.25 1z" fill="#1f6fc5"/></svg><span>1-604-555-0148</span></div>
      <div><svg width="14" height="12" viewBox="0 0 14 12"><rect x="0.5" y="0.5" width="13" height="11" fill="none" stroke="#1f6fc5"/><path d="M1 1l6 5 6-5" fill="none" stroke="#1f6fc5"/></svg><span>info@coralridgenet.ca</span></div>
    </div>
  </div>
  <div class="form">
    <div class="field" style="left:0;top:0;width:238px">Name</div>
    <div class="field" style="left:258px;top:0;width:238px">Phone number</div>
    <div class="field" style="left:0;top:62px;width:238px">Email Address</div>
    <div class="field" style="left:0;top:124px;width:496px;height:104px">Message</div>
    <div class="send">Send to</div>
  </div>
</section>

<footer class="footer">
  <div class="brand-box"><span>Coral Ridge</span></div>
  <div class="fcol" style="left:540px">
    <h4>Quick Links</h4>
    <ul><li>Home</li><li>About Us</li><li>Services</li><li>Contact</li></ul>
    <div class="socials"><i></i><i></i><i></i></div>
  </div>
  <div class="fcol" style="left:700px">
    <h4>Contact Us</h4>
    <div class="row"><svg width="11" height="11" viewBox="0 0 24 24"><path d="M6.6 10.8a15 15 0 0 0 6.6 6.6l2.2-2.2a1 1 0 0 1 1-.25 11.4 11.4 0 0 0 3.6.57 1 1 0 0 1 1 1V20a1 1 0 0 1-1 1A17 17 0 0 1 3 4a1 1 0 0 1 1-1h3.5a1 1 0 0 1 1 1c0 1.25.2 2.45.57 3.57a1 1 0 0 1-.25 1z" fill="#1f6fc5"/></svg>1-604-555-0148</div>
    <div class="row"><svg width="12" height="10" viewBox="0 0 14 12"><rect x="0.5" y="0.5" width="13" height="11" fill="none" stroke="#1f6fc5"/><path d="M1 1l6 5 6-5" fill="none" stroke="#1f6fc5"/></svg>info@coralridgenet.ca</div>
  </div>
  <div class="fcol" style="left:900px">
    <h4>Our Location</h4>
    <div style="line-height:18px">4120 Harbour Ave, Surrey,<br>BC V3S 2K7</div>
    <div role="img" aria-label="Map showing the office location" style="margin-top:12px;width:140px;height:84px;background:linear-gradient(135deg,#e7eaed,#c9d0d6)"></div>
  </div>
  <div class="rule"></div>
  <div class="copyright">Copyright 2022 Coral Ridge Ltd All Rights Reserved</div>
</footer>

</body>
</html>
```